Morrow Engineering Core Values Branding Package

Morrow Engineering has recently refined its company Core Values and is seeking a strong, cohesive branding package to visually bring these values to life. The new graphic assets will communicate our commitment to excellence in a way that resonates with our team, clients, and partners in a blue-collar, industrial environment.

We are looking for multiple visual assets with consistent design elements that can be applied across platforms. The tone should reflect strength, reliability, and professionalism while remaining approachable and aligned with our industry.

Core Values & Descriptions
Accountability
“We take ownership of our work and actions, ensuring reliability and trust in every solution we deliver.”

Teamwork
“We collaborate across departments and disciplines to provide the highest level of service and innovation for our clients.”

Integrity
“We operate with honesty, transparency, and ethical standards in all aspects of our business.”

Growth
“We are committed to continuous improvement—of our people, our processes, and our impact in the industry.”

Deliverables

1. Primary Core Values Graphic
A master visual representing all four values together.
Designed for use on posters, office signage, internal presentations.

2. Individual Value Graphics (x4)
One graphic per core value: Accountability, Teamwork, Integrity, Growth.
Cohesive style with slight visual variation to reflect each value’s unique meaning.

Target Market(s)

Employees of Morrow Engineering

Industry/Entity Type

Blue Collar

Font styles to use
Sans Serif

Colors
0054AA
0677BA
7BADD7
CADEEF
E8F1F8
00AB8E
00BBA5
67D7C9
C6EFE9
E9F9F6
EB3D1F
EC4F4E
F09395
F8D3D4
FCEDEE

Requirements
Must have
• Accountability, Teamwork, Integrity, Growth

```html
<!DOCTYPE html>
<html lang="en">
<head>
<meta charset="utf-8">
<title>Morrow Engineering – Core Values</title>
<link rel="stylesheet" href="https://fonts.googleapis.com/css2?family=Anton&family=Arimo:wght@700&display=swap">
<style>
  :root {
    --navy: #0b3264;
    --green: #3aae2b;
    --white: #ffffff;
    --icon-on-navy: #25497a;
    --icon-on-green: #5bbd4e;
  }
  * { box-sizing: border-box; margin: 0; padding: 0; }
  html, body { width: 731px; height: 1200px; overflow: hidden; background: var(--white); }
  .poster {
    position: relative;
    width: 731px;
    height: 1200px;
    background: var(--white);
    font-family: "Arimo", Arial, sans-serif;
  }
  .lower-band {
    position: absolute;
    left: 0; right: 0; top: 540px; bottom: 0;
    background: var(--navy);
  }
  .brand-name {
    position: absolute;
    top: 66px; left: 0; right: 0;
    text-align: center;
    font-family: "Anton", Impact, sans-serif;
    font-size: 50px;
    line-height: 1;
    color: var(--navy);
    letter-spacing: 1px;
  }
  .headline {
    position: absolute;
    top: 196px; left: 0; right: 0;
    text-align: center;
    font-family: "Anton", Impact, sans-serif;
    font-size: 128px;
    line-height: 1;
    transform: scaleY(1.28);
    transform-origin: top center;
    letter-spacing: -1px;
  }
  .headline .core { color: var(--green); }
  .headline .values { color: var(--navy); }
  .values-frame {
    position: absolute;
    left: 39px; top: 352px;
    width: 652px; height: 762px;
    border: 4px solid var(--white);
    border-radius: 8px;
  }
  .value-tile {
    position: absolute;
    width: 315px; height: 368px;
    text-align: center;
    color: var(--white);
    border-radius: 3px;
  }
  .value-tile.navy { background: var(--navy); }
  .value-tile.green { background: var(--green); }
  .tile-tl { left: 46px;  top: 358px; }
  .tile-tr { left: 368px; top: 358px; }
  .tile-bl { left: 46px;  top: 736px; }
  .tile-br { left: 368px; top: 736px; }
  .value-icon {
    display: block;
    margin: 62px auto 0;
    width: 116px; height: 118px;
  }
  .value-title {
    margin-top: 52px;
    font-family: "Anton", Impact, sans-serif;
    font-size: 30px;
    line-height: 1;
    font-weight: 400;
    transform: scaleY(1.15);
  }
  .value-text {
    margin: 14px auto 0;
    width: 270px;
    font-size: 13.5px;
    line-height: 1.45;
  }
  .site-url {
    position: absolute;
    left: 0; right: 0; top: 1150px;
    text-align: center;
    color: var(--white);
    font-size: 17px;
    letter-spacing: 4px;
  }
</style>
</head>
<body>
<main class="poster">
  <div class="lower-band"></div>

  <div class="brand-name">MORROW</div>

  <h1 class="headline"><span class="core">CORE</span> <span class="values">VALUES</span></h1>

  <div class="values-frame"></div>

  <section class="value-tile navy tile-tl">
    <svg class="value-icon" viewBox="0 0 116 118" role="img" aria-label="Icon: magnifier over document with person and cycle arrows">
      <rect width="116" height="118" rx="58" fill="var(--icon-on-navy)"/>
    </svg>
    <h2 class="value-title">ACCOUNTABILITY:</h2>
    <p class="value-text">We take ownership of our work and actions, ensuring reliability and trust in every solution we deliver.</p>
  </section>

  <section class="value-tile green tile-tr">
    <svg class="value-icon" viewBox="0 0 116 118" role="img" aria-label="Icon: two hands clasped in a firm handshake">
      <rect width="116" height="118" rx="58" fill="var(--icon-on-green)"/>
    </svg>
    <h2 class="value-title">TEAMWORK:</h2>
    <p class="value-text">We collaborate across departments and disciplines to provide the highest level of service and innovation for our clients.</p>
  </section>

  <section class="value-tile green tile-bl">
    <svg class="value-icon" viewBox="0 0 116 118" role="img" aria-label="Icon: gear with circular arrows and two people">
      <rect width="116" height="118" rx="58" fill="var(--icon-on-green)"/>
    </svg>
    <h2 class="value-title">INTEGRITY:</h2>
    <p class="value-text">We operate with honesty, transparency, and ethical standards in all aspects of our business.</p>
  </section>

  <section class="value-tile navy tile-br">
    <svg class="value-icon" viewBox="0 0 116 118" role="img" aria-label="Icon: three upward arrows rising from a road">
      <rect width="116" height="118" rx="58" fill="var(--icon-on-navy)"/>
    </svg>
    <h2 class="value-title">GROWTH:</h2>
    <p class="value-text">We are committed to continuous improvement—of our people, our processes, and our impact in the industry.</p>
  </section>

  <p class="site-url">WWW.MORROW-ENG.COM</p>
</main>
</body>
</html>
```